Local primary school needs a flyer design for their fundraising fete

I need a flyer design for a local primary school holding a fundraising fete. I would like to see designs that feature the school logo, school colours (red white and navy) and that reference/mention the main rides and stalls at the event. If possible I would like the sponsors (on the newsletter supplied) to be included and the photo of the school available on the website. The final design should be easy for me to print and produce myself so that can leave at local shops, cafes etc. leading up to the event.

Industry/Entity Type

School

Font styles to use
Serif

Colors
ec2027
ffffff

```html
<!DOCTYPE html>
<html lang="en">
<head>
<meta charset="utf-8">
<title>Holy Cross Primary School Fete Flyer</title>
<link rel="stylesheet" href="https://fonts.googleapis.com/css2?family=Arimo:wght@400;700&family=Libre+Baskerville:wght@400;700&display=swap">
<style>
  :root {
    --red: #ec2027;
    --deep-red: #a5121a;
    --white: #ffffff;
    --navy: #1c2a55;
    --ink: #3a3d45;
    --sky-top: #e9f0f5;
    --sky-bottom: #cfdde8;
    --page-bg: #ece8e2;
  }
  * { box-sizing: border-box; margin: 0; padding: 0; }
  html, body { width: 1200px; height: 1000px; overflow: hidden; }
  body {
    background: var(--page-bg);
    font-family: "Arimo", Arial, sans-serif;
    display: flex; align-items: center; justify-content: center;
  }
  .sheet {
    width: 1110px; height: 860px;
    display: flex; gap: 0;
    background: var(--white);
    box-shadow: 0 4px 18px rgba(0,0,0,.15);
  }
  .flyer {
    flex: 1; display: flex; flex-direction: column;
    border-right: 1px dashed #d6d6d6;
    background: linear-gradient(180deg, var(--sky-top), var(--sky-bottom));
  }
  .flyer:last-child { border-right: none; }
  .school-header {
    position: relative; height: 150px;
    background: linear-gradient(160deg, #6f8fb3 0%, #a9b9c8 45%, #8a5a4c 75%, #5d5d62 100%);
    display: flex; align-items: center; gap: 12px; padding: 0 18px;
  }
  .school-mark {
    width: 54px; height: 54px; border-radius: 50%;
    background: var(--red); border: 3px solid var(--white); flex: none;
  }
  .school-name {
    font-family: "Libre Baskerville", Georgia, serif;
    color: var(--white); font-size: 20px; font-weight: 700; line-height: 1.2;
    text-shadow: 0 1px 3px rgba(0,0,0,.45);
  }
  .red-rule { height: 12px; background: var(--deep-red); }
  .bunting {
    height: 46px; margin: 6px 16px 0;
    background: linear-gradient(90deg, #f4b6c8, #f8e38a, #b9dff2, #cfe9a8, #f4b6c8);
    opacity: .55; border-radius: 0 0 40px 40px;
  }
  .details {
    flex: 1; padding: 22px 24px 0;
    color: var(--ink); font-size: 13px; font-weight: 700; line-height: 1.55;
  }
  .details p { margin-bottom: 14px; }
  .highlight { color: var(--red); }
  .tents {
    position: relative; height: 210px;
    background: linear-gradient(180deg, rgba(255,255,255,0) 0%, #e9c6bd 35%, #c9473f 100%);
  }
  .sponsor-box {
    position: absolute; left: 22px; right: 22px; bottom: 14px; height: 120px;
    background: var(--white); border-radius: 14px;
    padding: 14px; display: grid; grid-template-columns: 1fr 1fr; gap: 8px 10px;
    align-content: center;
  }
  .sponsor {
    display: flex; align-items: center; gap: 6px;
    font-size: 11px; font-weight: 700; color: var(--navy);
  }
  .sponsor::before {
    content: ""; width: 10px; height: 10px; background: var(--navy); flex: none;
  }
  .sponsor-footer {
    height: 58px; background: var(--deep-red);
    color: var(--white); font-size: 15px; font-weight: 700;
    display: flex; align-items: center; justify-content: center;
  }
</style>
</head>
<body>
<main class="sheet">
  <section class="flyer">
    <header class="school-header" role="img" aria-label="Photograph of the school building">
      <span class="school-mark"></span>
      <h1 class="school-name">Holy Cross<br>Primary School</h1>
    </header>
    <div class="red-rule"></div>
    <div class="bunting" role="img" aria-label="Strings of colourful bunting flags"></div>
    <div class="details">
      <p><span class="highlight">Holy Cross Primary School</span> in Larchfield will hold their biannual fete on Sunday 21 September from 11.00am to 3.00pm.</p>
      <p>There will be some fantastic rides, including <span class="highlight">jumping castles, horizontal bungy</span> and if you're game, even a <span class="highlight">wild bucking bull!</span></p>
      <p>There will also be the old fete favourites, including the <span class="highlight">petting zoo, arts and craft,</span> the <span class="highlight">chocolate wheel</span> and the <span class="highlight">cake stall</span> to name a few along with other wonderful sweets and delicious foods to eat.</p>
      <p>With over <span class="highlight">20 stalls</span>, there will be something for everyone. So come along for a family excursion filled with fun and some bargain buys too.</p>
    </div>
    <div class="tents" role="img" aria-label="Illustration of red and white striped circus tents">
      <div class="sponsor-box">
        <span class="sponsor">Brightway Motors</span>
        <span class="sponsor">Northgate Dental</span>
        <span class="sponsor">Zenith Print</span>
        <span class="sponsor">Appleby Pharmacy</span>
        <span class="sponsor">Larch Realty</span>
        <span class="sponsor">Summit Sports</span>
      </div>
    </div>
    <footer class="sponsor-footer">2014 holy cross fete gold &amp; silver sponsors</footer>
  </section>

  <section class="flyer">
    <header class="school-header" role="img" aria-label="Photograph of the school building">
      <span class="school-mark"></span>
      <h1 class="school-name">Holy Cross<br>Primary School</h1>
    </header>
    <div class="red-rule"></div>
    <div class="bunting" role="img" aria-label="Strings of colourful bunting flags"></div>
    <div class="details">
      <p><span class="highlight">Holy Cross Primary School</span> in Larchfield will hold their biannual fete on Sunday 21 September from 11.00am to 3.00pm.</p>
      <p>There will be some fantastic rides, including <span class="highlight">jumping castles, horizontal bungy</span> and if you're game, even a <span class="highlight">wild bucking bull!</span></p>
      <p>There will also be the old fete favourites, including the <span class="highlight">petting zoo, arts and craft,</span> the <span class="highlight">chocolate wheel</span> and the <span class="highlight">cake stall</span> to name a few along with other wonderful sweets and delicious foods to eat.</p>
      <p>With over <span class="highlight">20 stalls</span>, there will be something for everyone. So come along for a family excursion filled with fun and some bargain buys too.</p>
    </div>
    <div class="tents" role="img" aria-label="Illustration of red and white striped circus tents">
      <div class="sponsor-box">
        <span class="sponsor">Brightway Motors</span>
        <span class="sponsor">Northgate Dental</span>
        <span class="sponsor">Zenith Print</span>
        <span class="sponsor">Appleby Pharmacy</span>
        <span class="sponsor">Larch Realty</span>
        <span class="sponsor">Summit Sports</span>
      </div>
    </div>
    <footer class="sponsor-footer">2014 holy cross fete gold &amp; silver sponsors</footer>
  </section>

  <section class="flyer">
    <header class="school-header" role="img" aria-label="Photograph of the school building">
      <span class="school-mark"></span>
      <h1 class="school-name">Holy Cross<br>Primary School</h1>
    </header>
    <div class="red-rule"></div>
    <div class="bunting" role="img" aria-label="Strings of colourful bunting flags"></div>
    <div class="details">
      <p><span class="highlight">Holy Cross Primary School</span> in Larchfield will hold their biannual fete on Sunday 21 September from 11.00am to 3.00pm.</p>
      <p>There will be some fantastic rides, including <span class="highlight">jumping castles, horizontal bungy</span> and if you're game, even a <span class="highlight">wild bucking bull!</span></p>
      <p>There will also be the old fete favourites, including the <span class="highlight">petting zoo, arts and craft,</span> the <span class="highlight">chocolate wheel</span> and the <span class="highlight">cake stall</span> to name a few along with other wonderful sweets and delicious foods to eat.</p>
      <p>With over <span class="highlight">20 stalls</span>, there will be something for everyone. So come along for a family excursion filled with fun and some bargain buys too.</p>
    </div>
    <div class="tents" role="img" aria-label="Illustration of red and white striped circus tents">
      <div class="sponsor-box">
        <span class="sponsor">Brightway Motors</span>
        <span class="sponsor">Northgate Dental</span>
        <span class="sponsor">Zenith Print</span>
        <span class="sponsor">Appleby Pharmacy</span>
        <span class="sponsor">Larch Realty</span>
        <span class="sponsor">Summit Sports</span>
      </div>
    </div>
    <footer class="sponsor-footer">2014 holy cross fete gold &amp; silver sponsors</footer>
  </section>
</main>
</body>
</html>
```